Business Card Design Project

We consult with hotels on setting rates and maximizing a revenue strategy

Industry/Entity Type

Business

Contact Information for Business Card

I am not sure what I want. Our company offers high level consulting to hotels around the country but we are also laid back. I would like something that is professional but also shows the laid back side

```html
<!DOCTYPE html>
<html lang="en">
<head>
<meta charset="utf-8">
<title>Harborline Business Card</title>
<link rel="stylesheet" href="https://fonts.googleapis.com/css2?family=Lato:ital,wght@0,400;0,700;1,400&family=PT+Sans+Narrow:wght@700&display=swap">
<style>
  :root {
    --page: #ffffff;
    --card-top: #35242f;
    --card-mid: #4a3f86;
    --card-base: #454c9f;
    --teal: #6cc4bc;
    --white: #ffffff;
  }
  * { margin: 0; padding: 0; box-sizing: border-box; }
  html, body {
    width: 1200px; height: 511px; overflow: hidden;
    background: var(--page);
  }
  .sheet { position: relative; width: 1200px; height: 511px; }
  .card {
    position: absolute; top: 39px; width: 562px; height: 338px;
    background: linear-gradient(180deg, var(--card-top) 0%, var(--card-mid) 28%, var(--card-base) 55%, var(--card-base) 100%);
    overflow: hidden;
    color: var(--white);
  }
  .card--front { left: 0; }
  .card--back { left: 636px; width: 564px; }

  .company-name {
    position: absolute;
    font-family: "Lato", sans-serif;
    font-weight: 700;
    color: var(--teal);
    letter-spacing: 2px;
    line-height: 1;
    white-space: nowrap;
  }
  .tagline {
    position: absolute;
    font-family: "PT Sans Narrow", "Arial Narrow", sans-serif;
    font-weight: 700;
    color: var(--white);
    line-height: 1;
    white-space: nowrap;
  }
  .stars { position: absolute; left: 0; top: 0; }

  /* front */
  .card--front .company-name { left: 40px; top: 46px; font-size: 46px; }
  .card--front .tagline { left: 51px; top: 98px; font-size: 22px; }
  .person { position: absolute; left: 53px; top: 212px; font-family: "Lato", sans-serif; }
  .person__name { font-size: 31px; font-weight: 700; line-height: 1.05; }
  .person__title { font-size: 17px; font-weight: 400; line-height: 1.2; }
  .contact {
    position: absolute; right: 43px; top: 218px;
    font-family: "Lato", sans-serif; font-style: italic;
    font-size: 15px; line-height: 20px; text-align: right;
  }
  .contact__label { margin-right: 4px; }

  /* back */
  .card--back .company-name { left: 201px; top: 140px; font-size: 44px; }
  .card--back .tagline { left: 211px; top: 195px; font-size: 23px; }
  .website {
    position: absolute; left: 209px; top: 250px;
    font-family: "Lato", sans-serif; font-size: 24px; color: var(--teal);
    white-space: nowrap;
  }
</style>
</head>
<body>
<div class="sheet">

  <section class="card card--front">
    <div class="company-name">HARBORLINE</div>
    <div class="tagline">Revenue Management Solutions</div>
    <svg class="stars" width="562" height="338" aria-hidden="true">
      <defs>
        <polygon id="star" points="0,-9 2.6,-3 9,-2.8 4.1,1.4 5.6,8 0,4.5 -5.6,8 -4.1,1.4 -9,-2.8 -2.6,-3" fill="#6cc4bc"/>
      </defs>
      <use href="#star" x="58" y="151"/>
      <use href="#star" x="143" y="151"/>
      <use href="#star" x="229" y="151"/>
      <use href="#star" x="323" y="151"/>
      <use href="#star" x="414" y="151"/>
    </svg>
    <div class="person">
      <div class="person__name">Dana Whitfield</div>
      <div class="person__title">Regional Revenue Manager</div>
    </div>
    <div class="contact">
      <div>Dana@HarborlineRMS.com</div>
      <div><span class="contact__label">office :</span> 503-555-0148</div>
      <div><span class="contact__label">fax :</span> 503-555-0193</div>
    </div>
  </section>

  <section class="card card--back">
    <svg class="stars" width="564" height="338" aria-hidden="true">
      <defs>
        <polygon id="star-back" points="0,-9 2.6,-3 9,-2.8 4.1,1.4 5.6,8 0,4.5 -5.6,8 -4.1,1.4 -9,-2.8 -2.6,-3" fill="#6cc4bc"/>
      </defs>
      <use href="#star-back" x="109" y="69"/>
      <use href="#star-back" x="194" y="69"/>
      <use href="#star-back" x="279" y="69"/>
      <use href="#star-back" x="374" y="69"/>
      <use href="#star-back" x="464" y="69"/>
    </svg>
    <div class="company-name">HARBORLINE</div>
    <div class="tagline">Revenue Management Solutions</div>
    <div class="website">www.HarborlineRMS.com</div>
  </section>

</div>
</body>
</html>
```